German Headhunter/ HR Consultancy needs Business Cards Design

We need a business Card Design for our Company in Stuttgart. We are specialized as Headhunter/ HR Consultancy in Placement of specialist and managers in permanent employment. Please refer to our business logo.

```html
<!DOCTYPE html>
<html lang="de">
<head>
<meta charset="utf-8">
<title>Business Card – Kernwerk Personalberatung</title>
<link href="https://fonts.googleapis.com/css2?family=Arimo:wght@400;700&display=swap" rel="stylesheet">
<style>
  :root {
    --page-bg: #e9e6e0;
    --navy-deep: #141f4d;
    --navy-mid: #1d2f78;
    --royal: #2541a3;
    --sand: #d8ccb4;
    --sand-light: #ece3d1;
    --pale-band: #dcdcdc;
    --cream-text: #efe6d6;
    --tan-text: #c2a880;
    --brand-navy: #1e2b62;
  }
  * { margin: 0; padding: 0; box-sizing: border-box; }
  html, body {
    width: 1200px; height: 927px; overflow: hidden;
    background: var(--page-bg);
    font-family: "Arimo", Arial, sans-serif;
  }
  .business-card {
    position: absolute; left: 50px; top: 156px;
    width: 1100px; height: 614px; overflow: hidden;
    background:
      radial-gradient(ellipse 420px 380px at 330px 300px, var(--royal) 0%, transparent 75%),
      linear-gradient(180deg, var(--navy-mid) 0%, var(--navy-mid) 60%, var(--navy-deep) 100%);
    box-shadow: 0 12px 30px rgba(0,0,0,.25);
  }
  .card-shapes { position: absolute; inset: 0; }
  .contact-block { position: absolute; left: 74px; top: 0; color: var(--cream-text); }
  .person-name {
    position: absolute; top: 109px; white-space: nowrap;
    font-size: 35px; font-weight: 700; letter-spacing: .3px;
  }
  .person-role { position: absolute; top: 152px; font-size: 28px; white-space: nowrap; }
  .address { position: absolute; top: 253px; font-size: 28px; line-height: 35px; white-space: nowrap; }
  .contact-list { position: absolute; top: 382px; list-style: none; }
  .contact-list li {
    display: flex; align-items: center; height: 42px;
    font-size: 28px; white-space: nowrap;
  }
  .contact-list svg { width: 26px; height: 26px; margin-right: 16px; flex: none; }
  .contact-list .email, .contact-list .web { color: var(--tan-text); }
  .brand {
    position: absolute; left: 560px; top: 266px;
    display: flex; align-items: center; gap: 70px;
    color: var(--brand-navy);
  }
  .brand-square { width: 62px; height: 62px; background: var(--brand-navy); flex: none; }
  .brand-name { font-weight: 700; line-height: 1; }
  .brand-name .line-main { display: block; font-size: 54px; letter-spacing: 1px; }
  .brand-name .line-sub { display: block; font-size: 26px; margin-top: 6px; letter-spacing: -.2px; }
</style>
</head>
<body>
  <section class="business-card">
    <svg class="card-shapes" viewBox="0 0 1100 614" width="1100" height="614">
      <defs>
        <linearGradient id="sandGrad" x1="0" y1="0" x2="1" y2="0">
          <stop offset="0" stop-color="var(--sand)"/>
          <stop offset="1" stop-color="var(--sand-light)"/>
        </linearGradient>
      </defs>
      <polygon class="pale-chevron" points="791,0 1100,0 1100,614 791,614 479,313" fill="var(--pale-band)"/>
      <polygon class="sand-panel" points="830,0 1100,0 1100,614 830,614 530,313" fill="url(#sandGrad)"/>
    </svg>

    <div class="contact-block">
      <h1 class="person-name">MARTIN KELLER</h1>
      <p class="person-role">Manager</p>
      <p class="address">Your address, city<br>state, ZIP 0000</p>
      <ul class="contact-list">
        <li class="phone">
          <svg viewBox="0 0 24 24" aria-hidden="true"><path fill="var(--cream-text)" d="M6.6 10.8c1.4 2.8 3.8 5.1 6.6 6.6l2.2-2.2c.3-.3.7-.4 1-.2 1.1.4 2.3.6 3.6.6.6 0 1 .4 1 1V20c0 .6-.4 1-1 1C10.6 21 3 13.4 3 4c0-.6.4-1 1-1h3.5c.6 0 1 .4 1 1 0 1.3.2 2.5.6 3.6.1.3 0 .7-.2 1z"/></svg>
          0711-555-0142
        </li>
        <li class="email">
          <svg viewBox="0 0 24 24" aria-hidden="true"><path fill="var(--cream-text)" d="M2 5h20v14H2z"/><path fill="none" stroke="var(--navy-mid)" stroke-width="1.6" d="M2 5l10 8 10-8M2 19l7-7M22 19l-7-7"/></svg>
          youremail@mailhub.com
        </li>
        <li class="web">
          <svg viewBox="0 0 24 24" aria-hidden="true"><circle cx="12" cy="12" r="10" fill="var(--tan-text)"/><circle cx="12" cy="12" r="4" fill="var(--navy-mid)"/></svg>
          www.yourwebsite.com
        </li>
      </ul>
    </div>

    <div class="brand">
      <span class="brand-square" aria-hidden="true"></span>
      <p class="brand-name"><span class="line-main">KERNWERK</span><span class="line-sub">PERSONALBERATUNG</span></p>
    </div>
  </section>
</body>
</html>
```